Website background design for music entertainment company

We are an events management company specialising in live music bookings. We connect music bands with venues and facilitate the arrangements.

We require a background image to use on our website. The template theme we are working with is http://layoutbazaar.example/item/vantor-stage-sound-site-theme/full_screen_preview/5810264

I have attached images of the current website homepage layout and the finalised logo. Ideally we would like the website background to work in well with the logo to create an overall feeling of music and an energetic feeling, but without being too overwhelming.

The music we will be providing to venues is mainly soft acoustic music for weddings and corporate events and rock music for bars, not really music for night clubs or large rock concerts. So we don't want our homepage to have too much of a "party" "nightclub" or "rock concert feeling". We would like it to be versatile to multiple styles of music and types of venues if possible.

We would like for the designers to try using either one of these two stock images, but enhance them with some colour. But we feel that these images are too dull as they are.
We are happy to purchase one, if it works well in any of the submissions.

http://www.pictovault.example/photo/rock-guitarist-52817046?st=7c4e2b9
http://www.pictovault.example/photo/bass-guitar-on-black-background-lesson-60391572?st=e5d8f13
Updates

Hi designers, We have updated our project to committed payment. We look forward to seeing designs :)

Target Market(s)

Target market is as follows:
1. Venue managers for pubs, bars, function centres, wedding venues.
2. Musicians, entertainers.
3. Brides, wedding planners.

Industry/Entity Type

Entertainment

Colors
add136
9bcb3c
fbee3e
fbed22
33a7d8
4daddb

Requirements
Must have
• 1. Communicates "energetic"
2. Communicates "music"
3. Works well with website template overall image
4. Works well with logo
Should not have
• Should not be too "cartoon-like" or have too much of a "nightclub or "large concert" feeling.

```html
<!DOCTYPE html>
<html lang="en">
<head>
<meta charset="utf-8">
<title>Velora Entertainment</title>
<link rel="stylesheet" href="https://fonts.googleapis.com/css2?family=Dosis:wght@300;400;500;600&display=swap">
<style>
:root{
  --cyan:#1fd0c6;
  --nav-active:#17c4e8;
  --ink:#ffffff;
  --muted:#8a8f8c;
  --body:#c9cfcc;
  --panel:rgba(6,12,9,.72);
  --card:#050807;
  --btn:#2c2f2e;
  --rule:#3a3f3c;
  --lime:#b8e04a;
  --leaf:#3f9a66;
}
*{margin:0;padding:0;box-sizing:border-box}
html,body{width:1200px;height:1000px;overflow:hidden}
body{position:relative;font-family:"Dosis",sans-serif;color:var(--ink);background:#0c2a1a}
.backdrop{position:absolute;inset:0;background:
  radial-gradient(circle 60px at 1110px 140px,rgba(235,245,120,.55),transparent 80%),
  radial-gradient(circle 70px at 880px 60px,rgba(200,235,110,.4),transparent 80%),
  radial-gradient(ellipse 320px 260px at 1060px 200px,rgba(170,220,90,.5),transparent 70%),
  radial-gradient(ellipse 240px 180px at 1150px 560px,rgba(120,200,110,.45),transparent 70%),
  radial-gradient(ellipse 420px 300px at 40px 330px,rgba(110,200,140,.55),transparent 70%),
  radial-gradient(ellipse 300px 380px at 120px 860px,rgba(90,180,130,.5),transparent 70%),
  radial-gradient(ellipse 250px 420px at 1120px 820px,rgba(70,160,100,.45),transparent 70%),
  linear-gradient(135deg,#1f6043,#0d3322 55%,#16503a)}
.backdrop-strings{position:absolute;inset:0;opacity:.9}
.site-header{position:absolute;left:0;top:0;width:1200px;height:115px;background:rgba(8,14,11,.93)}
.brand{position:absolute;left:170px;top:42px;display:flex;align-items:center;gap:9px}
.brand-mark{width:12px;height:12px;background:var(--cyan)}
.brand-name{font-size:20px;font-weight:500;letter-spacing:1px;color:var(--cyan);white-space:nowrap}
.main-nav{position:absolute;left:484px;top:40px;height:32px}
.main-nav a{position:absolute;top:0;height:32px;line-height:32px;font-size:13.5px;font-weight:500;color:#e6e6e6;text-decoration:none;text-transform:uppercase;text-align:center;letter-spacing:.3px}
.main-nav a.active{background:var(--nav-active);color:#fff}
.main-nav a.boxed{background:var(--btn)}
.content{position:absolute;left:145px;top:148px;width:897px;height:852px;background:var(--panel)}
.slider{position:absolute;left:163px;top:166px;width:860px;height:353px;background:
  radial-gradient(ellipse 260px 140px at 430px 110px,#4a7cff,transparent 70%),
  linear-gradient(180deg,#1b2a6b 0%,#0f1a44 55%,#07091a 100%)}
.slider-arrow{position:absolute;top:159px;width:36px;height:36px;background:rgba(0,0,0,.7)}
.slider-arrow svg{display:block;margin:10px auto}
.slide-title{position:absolute;left:233px;top:401px;height:44px;padding:0 14px;background:var(--cyan);font-size:31px;font-weight:500;line-height:44px;text-transform:uppercase}
.slide-sub{position:absolute;left:247px;top:454px;font-size:18px;font-weight:500;text-transform:uppercase}
.section-title{position:absolute;font-size:27px;font-weight:500;text-transform:uppercase}
.section-title span{color:var(--cyan)}
.post{position:absolute;left:165px;width:577px;height:174px;background:var(--card)}
.post-thumb{position:absolute;left:11px;top:14px;width:193px;height:146px}
.post-body{position:absolute;left:218px;top:12px;width:345px}
.post-title{font-size:21px;font-weight:500;line-height:26px}
.post-meta{display:flex;gap:18px;margin-top:7px;font-size:12.5px;font-weight:300;color:var(--muted)}
.post-meta span{display:flex;align-items:center;gap:5px}
.post-excerpt{margin-top:8px;font-size:12px;font-weight:300;line-height:18px;color:var(--body)}
.read-more{display:inline-block;margin-top:8px;height:28px;line-height:28px;padding:0 7px;background:var(--btn);font-size:12.5px;text-transform:uppercase;color:#e6e6e6}
.player{position:absolute;left:761px;top:597px;width:262px;height:295px;background:var(--card)}
.album-art{position:absolute;left:12px;top:12px;width:92px;height:90px;background:radial-gradient(circle at 60% 55%,#3ab4d8,#0f5c78 60%,#0a2a36)}
.album-info{position:absolute;left:112px;top:6px}
.album-title{font-size:15px;font-weight:500}
.album-detail{font-size:12px;font-weight:300;color:var(--muted);line-height:20px;margin-top:2px}
.store-links{display:flex;gap:3px;margin-top:7px}
.store-links span{height:26px;line-height:26px;padding:0 7px;background:var(--btn);font-size:12px;text-transform:uppercase;color:#e6e6e6}
.player-bar{position:absolute;left:12px;top:115px;width:239px;height:23px;background:#2f3231;display:flex;align-items:center}
.play{width:28px;height:23px;border-right:1px solid #555;display:flex;align-items:center;justify-content:center}
.track{margin:0 12px 0 10px;flex:1;height:4px;background:#111}
.time{font-size:10px;color:#ddd;padding-right:8px;letter-spacing:.5px}
.time em{font-style:normal;color:var(--muted)}
.playlist{position:absolute;left:15px;top:145px;width:236px;list-style:none}
.playlist li{height:27px;line-height:27px;font-size:12px;font-weight:300;color:#d9dcda;border-bottom:1px dashed var(--rule)}
.playlist li:last-child{border-bottom:none}
.event{position:absolute;left:761px;top:972px;width:262px;height:40px;background:var(--card)}
.event-day{position:absolute;left:14px;top:6px;font-size:30px;font-weight:300;color:#6c716e}
.event-divider{position:absolute;left:66px;top:8px;width:1px;height:26px;border-left:1px dashed var(--rule)}
.event-name{position:absolute;left:78px;top:8px;font-size:16px;font-weight:400;color:#d9dcda}
</style>
</head>
<body>
<div class="backdrop" role="img" aria-label="Close-up of a guitar neck and strings in green and lime light with soft bokeh"></div>
<svg class="backdrop-strings" width="1200" height="1000" viewBox="0 0 1200 1000" aria-hidden="true">
  <defs>
    <linearGradient id="neck" x1="0" y1="0" x2="1" y2="1">
      <stop offset="0" stop-color="#8fd18a" stop-opacity=".0"/>
      <stop offset=".45" stop-color="#7cc98a" stop-opacity=".28"/>
      <stop offset="1" stop-color="#2f7a52" stop-opacity=".0"/>
    </linearGradient>
  </defs>
  <path d="M-60 720 L420 160 L560 260 L60 860 Z" fill="url(#neck)"/>
  <path d="M860 1000 L1200 560 L1200 760 L1000 1000 Z" fill="url(#neck)"/>
  <g stroke="#d8f0c0" stroke-opacity=".22" stroke-width="1.5" fill="none">
    <line x1="-20" y1="730" x2="450" y2="180"/>
    <line x1="0" y1="750" x2="470" y2="200"/>
    <line x1="20" y1="770" x2="490" y2="220"/>
    <line x1="40" y1="790" x2="510" y2="240"/>
    <line x1="890" y1="1000" x2="1200" y2="600"/>
    <line x1="915" y1="1000" x2="1200" y2="630"/>
    <line x1="940" y1="1000" x2="1200" y2="660"/>
  </g>
</svg>

<header class="site-header">
  <div class="brand"><div class="brand-mark"></div><div class="brand-name">VELORA ENTERTAINMENT</div></div>
  <nav class="main-nav">
    <a class="active" href="#" style="left:0;width:58px">Home</a>
    <a class="boxed" href="#" style="left:63px;width:153px">Hire Entertainment</a>
    <a class="boxed" href="#" style="left:222px;width:151px">Apply to Entertain</a>
    <a href="#" style="left:378px;width:78px">About Us</a>
    <a href="#" style="left:465px;width:94px">Contact Us</a>
  </nav>
</header>

<main class="content"></main>

<section class="slider" role="img" aria-label="Festival main stage lit in blue above a large crowd">
  <div class="slider-arrow" style="left:5px"><svg width="10" height="16" viewBox="0 0 10 16"><path d="M8 1 2 8l6 7" fill="none" stroke="#777" stroke-width="2"/></svg></div>
  <div class="slider-arrow" style="right:3px"><svg width="10" height="16" viewBox="0 0 10 16"><path d="M2 1l6 7-6 7" fill="none" stroke="#777" stroke-width="2"/></svg></div>
</section>
<div class="slide-title">Pulse Harbor Festival 2012</div>
<div class="slide-sub">Suspendisse scelerisque suscipit facilisis.</div>

<h2 class="section-title" style="left:163px;top:549px">Latest <span>Blog</span></h2>

<article class="post" style="top:595px">
  <div class="post-thumb" role="img" aria-label="DJ performing at a warm-lit festival booth" style="background:linear-gradient(135deg,#5a2a24,#b98a78 45%,#2a1412)"></div>
  <div class="post-body">
    <h3 class="post-title">Daybreak Festival organized Croatia 2012</h3>
    <div class="post-meta">
      <span><svg width="12" height="12" viewBox="0 0 12 12"><circle cx="6" cy="3.5" r="3" fill="#666"/><path d="M0 12c0-4 3-5.5 6-5.5S12 8 12 12z" fill="#666"/></svg>admin</span>
      <span><svg width="12" height="12" viewBox="0 0 12 12"><rect x="0.5" y="1.5" width="11" height="10" fill="none" stroke="#666"/><rect x="0.5" y="1.5" width="11" height="3" fill="#666"/></svg>November 13th, 2012</span>
      <span><svg width="14" height="12" viewBox="0 0 14 12"><ellipse cx="7" cy="5" rx="7" ry="5" fill="#666"/><path d="M3 8 2 12l5-3z" fill="#666"/></svg>0 Comments</span>
    </div>
    <p class="post-excerpt">Mauris iaculis porttitor posuere. Praesent id metus massa, ut blandit odio. Proin quis tortor orci. Etiam at risus et justo dignissim congue. Donec congue lacinia dui, a porttitor lectus ...</p>
    <span class="read-more">Read more</span>
  </div>
</article>

<article class="post" style="top:786px">
  <div class="post-thumb" role="img" aria-label="Performer in a striped top under green club light" style="background:linear-gradient(135deg,#1e4a36,#6a8c7a 50%,#1a1f22)"></div>
  <div class="post-body">
    <h3 class="post-title">Thousands celebrities at Marlow Night</h3>
    <div class="post-meta">
      <span><svg width="12" height="12" viewBox="0 0 12 12"><circle cx="6" cy="3.5" r="3" fill="#666"/><path d="M0 12c0-4 3-5.5 6-5.5S12 8 12 12z" fill="#666"/></svg>admin</span>
      <span><svg width="12" height="12" viewBox="0 0 12 12"><rect x="0.5" y="1.5" width="11" height="10" fill="none" stroke="#666"/><rect x="0.5" y="1.5" width="11" height="3" fill="#666"/></svg>November 13th, 2012</span>
      <span><svg width="14" height="12" viewBox="0 0 14 12"><ellipse cx="7" cy="5" rx="7" ry="5" fill="#666"/><path d="M3 8 2 12l5-3z" fill="#666"/></svg>2 Comments</span>
    </div>
    <p class="post-excerpt">libendum elit, eu euismod magna sapien ut nibh. Donec semper quam scelerisque tortor dictum gravida. In hac habitasse platea dictumst. Nam pulvinar, odio sed rhoncus suscipit, sem diam ultrices ...</p>
    <span class="read-more">Read more</span>
  </div>
</article>

<h2 class="section-title" style="left:148px;top:982px">Latest <span>Events</span></h2>

<h2 class="section-title" style="left:761px;top:549px">Audio <span>Player</span></h2>
<aside class="player">
  <div class="album-art" role="img" aria-label="Album cover with blue circular artwork"></div>
  <div class="album-info">
    <div class="album-title">Sensation Source</div>
    <div class="album-detail">Genre: Tech House<br>Release date: 13 Sep 2012</div>
    <div class="store-links"><span>Songshop</span><span>Trackdock</span></div>
  </div>
  <div class="player-bar">
    <div class="play"><svg width="9" height="10" viewBox="0 0 9 10"><path d="M0 0l9 5-9 5z" fill="#fff"/></svg></div>
    <div class="track"></div>
    <div class="time">00:00 / <em>08:47</em></div>
  </div>
  <ol class="playlist">
    <li>1. Do It Properly Peter Lindqvist Remix</li>
    <li>2. Larrys Exotic Blend Original Mix</li>
    <li>3. Kalanimo Original Mix4.</li>
    <li>4. Lost In Music Carlo Fenwick</li>
    <li>5. Exhale Original Mix</li>
  </ol>
</aside>

<h2 class="section-title" style="left:761px;top:924px">Upcoming <span>Events</span></h2>
<div class="event">
  <div class="event-day">24</div>
  <div class="event-divider"></div>
  <div class="event-name">Night Velvet Fridays</div>
</div>
</body>
</html>
```